Radiant Harvest Gathering 2021

I am looking to create a flyer for a one day prayer retreat our church is organizing. This flyer will be posted on social media, websites, mobile apps, and will also be printed so it can be mailed to people.

I am looking for something professional, with good use of our logo and band colors (logo colors).

I am counting on the designer's skill, creativity, art and knowledge of media communication to produce a flyer that will effectively and quickly convey the message we are trying to spread.

CONTENT OF THE FLYER:
Event title: Radiant Harvest Gathering
Date: Tuesday July 2nd, 2021
Time: 11:00AM - 7:00PM
Bellmore Hotel, 4817 Wexley Avenue, Portland, Maine 04109 (Room: Tamarind)
Event Key words to highlight what the event is about: Prayer, Fasting, Worship, Prophecy, Revival.
Key phrases:
A one day prayer retreat.
Jesus Chris is Lord

Contact info:
www.quvello.org
Phone: 207 555 0148
Email: contact@brookmeadow.org

```html
<!DOCTYPE html>
<html lang="en">
<head>
<meta charset="utf-8">
<title>Radiant Harvest Gathering 2021</title>
<link href="https://fonts.googleapis.com/css2?family=Yesteryear&family=Anton&family=Jost:wght@600&family=Roboto:wght@500&display=swap" rel="stylesheet">
<style>
  :root {
    --page: #e4e4e4;
    --navy: #0b3a5f;
    --ink: #15171b;
    --orange: #f7941d;
    --white: #ffffff;
    --photo-light: #56658a;
    --photo-dark: #1d2433;
  }
  * { margin: 0; padding: 0; box-sizing: border-box; }
  html, body { width: 1200px; height: 880px; overflow: hidden; background: var(--page); }
  .flyer {
    position: absolute; left: 290px; top: 20px; width: 620px; height: 840px;
    background: linear-gradient(180deg, var(--navy) 0%, #10304d 45%, var(--ink) 100%);
    box-shadow: 0 6px 18px rgba(0,0,0,.25);
    overflow: hidden; color: var(--white);
  }
  .brand {
    position: absolute; top: 30px; right: 28px; display: flex; align-items: center; gap: 6px;
    font-family: "Jost", sans-serif; font-weight: 600; font-size: 17px; letter-spacing: 1px; color: var(--white);
  }
  .brand-dot { width: 8px; height: 8px; border-radius: 50%; background: var(--orange); }
  .title-script {
    position: absolute; top: 40px; left: 28px;
    font-family: "Yesteryear", cursive; font-size: 64px; color: var(--orange); line-height: 1;
  }
  .title-main {
    position: absolute; top: 104px; left: 26px;
    font-family: "Anton", sans-serif; font-size: 98px; line-height: 1; letter-spacing: 2px;
    color: var(--white); text-shadow: -5px 0 0 var(--orange);
  }
  .tagline {
    position: absolute; top: 232px; left: 28px;
    font-family: "Jost", sans-serif; font-weight: 600; font-size: 22px; line-height: 1.3; letter-spacing: 1px;
    text-transform: uppercase;
  }
  .tagline em { font-style: normal; color: var(--orange); }
  .keywords {
    position: absolute; top: 300px; left: 22px; right: 40px; height: 32px;
    background: var(--orange); color: var(--navy);
    font-family: "Jost", sans-serif; font-weight: 600; font-size: 17px; letter-spacing: .5px;
    display: flex; align-items: center; justify-content: center; gap: 8px; text-transform: uppercase;
  }
  .photo {
    position: absolute; top: 345px; left: 0; width: 360px; height: 340px;
    background: radial-gradient(ellipse at 55% 40%, var(--photo-light) 0%, #36435f 45%, rgba(29,36,51,0) 80%);
  }
  .details { position: absolute; top: 390px; right: 36px; text-align: right; }
  .date-label { font-family: "Anton", sans-serif; font-size: 24px; }
  .date { font-family: "Anton", sans-serif; font-size: 36px; line-height: 1.15; }
  .time { font-family: "Anton", sans-serif; font-size: 22px; color: var(--orange); }
  .venue { position: absolute; top: 560px; right: 36px; text-align: right;
    font-family: "Jost", sans-serif; font-weight: 600; text-transform: uppercase; }
  .venue-name { font-size: 24px; color: var(--orange); letter-spacing: 1px; }
  .venue-line { font-size: 14px; line-height: 1.35; }
  .venue-room { font-size: 14px; color: var(--orange); }
  .contacts {
    position: absolute; bottom: 40px; left: 36px; right: 36px;
    display: flex; justify-content: space-between; align-items: center;
    font-family: "Roboto", sans-serif; font-weight: 500; font-size: 15px;
  }
  .contact { display: flex; align-items: center; gap: 8px; }
  .contact svg { width: 16px; height: 16px; fill: none; stroke: var(--white); stroke-width: 1.5; }
</style>
</head>
<body>
  <main class="flyer">
    <div class="brand"><span class="brand-dot"></span>QUVELLO</div>
    <h1>
      <span class="title-script">Radiant Harvest</span>
      <span class="title-main">GATHERING</span>
    </h1>
    <p class="tagline"><em>A</em> one day <em>prayer</em> retreat<br>Jesus <em>Chris is</em> Lord</p>
    <div class="keywords">
      <span>Prayer</span>|<span>Fasting</span>|<span>Worship</span>|<span>Prophecy</span>|<span>Revival</span>
    </div>
    <div class="photo" role="img" aria-label="Photo of praying hands holding a cross necklace"></div>
    <section class="details">
      <p class="date-label">Date: Tuesday</p>
      <p class="date">July 2nd, 2021</p>
      <p class="time">Time: 11:00AM - 7:00PM</p>
    </section>
    <address class="venue" style="font-style:normal">
      <p class="venue-name">Bellmore Hotel</p>
      <p class="venue-line">4817 Wexley Avenue<br>Portland<br>Maine 04109</p>
      <p class="venue-room">(Room: Tamarind)</p>
    </address>
    <footer class="contacts">
      <span class="contact">
        <svg viewBox="0 0 16 16"><circle cx="8" cy="8" r="6.5"/><ellipse cx="8" cy="8" rx="3" ry="6.5"/><line x1="1.5" y1="8" x2="14.5" y2="8"/></svg>
        www.quvello.org
      </span>
      <span class="contact">
        <svg viewBox="0 0 16 16"><path d="M2 6 Q8 1 14 6 L12 7.5 L10.5 5.5 L5.5 5.5 L4 7.5 Z" fill="#fff"/><rect x="4" y="8" width="8" height="6" rx="1" fill="#fff"/></svg>
        207 555 0148
      </span>
      <span class="contact">
        <svg viewBox="0 0 16 16"><rect x="1.5" y="3.5" width="13" height="9"/><polyline points="1.5,3.5 8,9 14.5,3.5"/></svg>
        contact@brookmeadow.org
      </span>
    </footer>
  </main>
</body>
</html>
```